Sticker label design for - Over Fleet Deodorant Balm

I need a label for my 100% Natural Deodorant Balm
The brand is called "Mild Meadow Brand", and the product is called OVER FLEET Deodorant Balm.
There are two labels, one is a 5.2cm circle for the top, and 4.5cm circle for the base. The jar is amber plastic with black lid.
Width: 5.8cm
Height: 3.4cm (Lid 1.2cm, base 2,2cm)
Here is a link to what the jar looks like from one of my competitors: https://redsparrow.com.au/products/body/crest-deodorant-paste/
The product is a unisex product. Please see uploaded files for designs previously made for the brand. I'm trying to see a few more designs before finalising my choice. Feel free to use the logo at the top (Mild Meadow Brand) of either attachment if you would like. Or design your own.
Be be aware that it is meant to be Aluminium and Paraben Free, not "Parabens" Weight of product is 70g, please include this.
Label can be any colour, and printed with regular colours or event gold, silver or rose gold foil. Would a background be nice?
This is something I saw that I liked:
http://www.tolvenbalm.com
However I'm really open to what people can come up with.
For the back base-
Over Fleet deodorant balm is made from 100% natural ingredients, and works by neutralises odour and minimising wetness without the use of harmful chemicals.
www.mildmeadowbrand.com
Directions: For optimal result, apply a pea size amount of the balm to your dry armpits. Gently rub the balm into your armpits covering the entire area. Discontinue use if irritation occurs.
Ingredients: Shea Butter, Coconut oil, Sodium Bicarbonate, Arrowroot, Kaolin Clay, Vitamin E, Vegetable Glycerin, Activated Charcoal, Essential oils of Peppermint, Lavender, Mandarin, Tea tree, Geranium Rose & Cedarwood.
MADE IN AUSTRALIA
Reason: Hi,
I'm not getting many submissions, so was hoping to extend the deadline.
Skin Care Product

```html
<!DOCTYPE html>
<html lang="en">
<head>
<meta charset="utf-8">
<title>Over Fleet Deodorant Balm – Lid Label</title>
<link rel="stylesheet" href="https://fonts.googleapis.com/css2?family=Montserrat:wght@300;700&family=Roboto+Condensed:wght@400&display=swap">
<style>
  :root {
    --page-bg: #ffffff;
    --label-ink: #231f20;
    --label-text: #ffffff;
  }
  html, body {
    margin: 0;
    padding: 0;
    width: 1200px;
    height: 1200px;
    overflow: hidden;
    background: var(--page-bg);
  }
  .canvas {
    display: block;
    width: 1200px;
    height: 1200px;
  }
  .label-disc { fill: var(--label-ink); }
  .brand-arc {
    font-family: "Montserrat", sans-serif;
    font-weight: 300;
    font-size: 19px;
    letter-spacing: 0.5px;
    fill: var(--label-text);
  }
  .product-title {
    font-family: "Montserrat", sans-serif;
    font-weight: 700;
    font-size: 35px;
    letter-spacing: 0.5px;
    fill: var(--label-text);
  }
  .net-weight {
    font-family: "Roboto Condensed", sans-serif;
    font-weight: 400;
    font-size: 13px;
    fill: var(--label-text);
  }
  .claims-ring {
    font-family: "Montserrat", sans-serif;
    font-weight: 300;
    font-size: 19px;
    letter-spacing: 1px;
    fill: var(--label-text);
  }
</style>
</head>
<body>
<svg class="canvas" viewBox="0 0 1200 1200" xmlns="http://www.w3.org/2000/svg">
  <defs>
    <path id="brand-path" d="M 470 505 A 330 330 0 0 1 730 505"/>
    <path id="claims-path" d="M 396.4 491.7 A 231 231 0 1 0 803.6 491.7"/>
  </defs>

  <circle class="label-disc" cx="600" cy="600" r="247"/>

  <text class="brand-arc" text-anchor="middle">
    <textPath href="#brand-path" startOffset="50%">MILD MEADOW BRAND</textPath>
  </text>

  <text class="product-title" x="600" y="564" text-anchor="middle">OVER FLEET</text>
  <text class="product-title" x="600" y="609" text-anchor="middle">DEODORANT BALM</text>

  <text class="net-weight" x="600" y="718" text-anchor="middle">NET WT. 2.4 OZ ℮ 70gms</text>

  <text class="claims-ring" text-anchor="middle">
    <textPath href="#claims-path" startOffset="50%">100 % NATURAL • ALUMINUM &amp; PARABEN FREE • VEGAN • CRUELTY FREE</textPath>
  </text>
</svg>
</body>
</html>
```